Financial Advisor needs waiting room sign

I am a financial advisor that works with a number of accountants to develop prospects. I am looking for a 18"x24" sign to hang in their office waiting rooms to help develop prospect interest in my services. My original idea was to list all of our services in a jumbled way on the sign and on the bottom have something like "Confused? We have the answers?" "Questions - We have answers" Our logo on the bottom. While I think this is still a good idea when I try to design it - it does not work. I am open to other ideas. Here is a list of our services (list in no particular order) and I will attach our logo. List: Plovance, Plovance Supplement, Plovance Advantage, Truvely, Part A, Part B, Part D, Social Security, Turning 65, Annuities, Fixed Index Annuities, Rollovers, 401k, 403b, Investments, Stock Market, Mutual Funds, Term Insurance, Life Insurance, Final Expense, Long Term Care, Mortgage Protection, 403B / 457 Not for Profit Set Up, 403B / TSA Plans, Annuities, Asset Protection, Charitable Giving, College Funding, Estate Planning, Fixed Indexed Annuities, Guaranteed Income, IRA & 401(K) Assets and Planning, IRA, 401(K), 403(B) Rollovers, Lifetime Income Planning, Retirement Income Planning, Safe Money Options, Social Security, Tactical Asset Allocation

```html
<!DOCTYPE html>
<html lang="en">
<head>
<meta charset="utf-8">
<title>Halvorn Capital – Our Services</title>
<link href="https://fonts.googleapis.com/css2?family=Lato:wght@400;700;900&display=swap" rel="stylesheet">
<style>
  :root {
    --green: #6aa83a;
    --green-light: #7cc241;
    --green-dark: #3f6b26;
    --ink: #141414;
    --panel-top: #333333;
    --panel-bottom: #1a1a1a;
    --white: #ffffff;
    --text-light: #e8e8e8;
    --footer-grey: #3a3a3a;
    --placeholder-tint: #8fc263;
  }
  * { box-sizing: border-box; margin: 0; padding: 0; }
  html, body { width: 1040px; height: 1200px; overflow: hidden; background: var(--white); }
  body { font-family: "Lato", sans-serif; }
  .sign { position: relative; width: 1040px; height: 1200px; overflow: hidden; background: var(--white); }
  .backdrop { position: absolute; inset: 0; width: 1040px; height: 1200px; }

  .illustration-slot { position: absolute; left: 108px; top: 24px; width: 202px; height: 138px; background: var(--placeholder-tint); border-radius: 8px; }

  .headline-confused { position: absolute; left: 36px; top: 190px; font-size: 64px; font-weight: 900; color: var(--ink); letter-spacing: -0.5px; line-height: 1; }
  .tagline-answers { position: absolute; left: 39px; top: 265px; font-size: 50px; font-weight: 400; color: var(--white); line-height: 58px; }
  .headline-questions { position: absolute; right: 48px; top: 36px; font-size: 72px; font-weight: 900; color: var(--ink); letter-spacing: -0.5px; line-height: 1; }
  .tagline-right { position: absolute; right: 61px; top: 135px; font-size: 56px; font-weight: 400; color: var(--green-light); text-align: right; line-height: 63px; }

  .services-title { position: absolute; left: 72px; top: 550px; font-size: 52px; font-weight: 900; color: var(--green); line-height: 1; }
  .service-list { position: absolute; list-style: none; color: var(--text-light); font-size: 23px; font-weight: 400; }
  .service-list li { position: relative; height: 30px; line-height: 30px; padding-left: 37px; white-space: nowrap; }
  .service-list li svg { position: absolute; left: 0; top: 8px; width: 16px; height: 16px; }
  .list-left { left: 74px; top: 659px; }
  .list-right { left: 551px; top: 510px; }

  .brand { position: absolute; left: 169px; top: 1088px; height: 84px; display: flex; align-items: center; }
  .brand-dot { width: 84px; height: 84px; border-radius: 50%; background: var(--green); }
  .brand-divider { width: 2px; height: 66px; background: var(--footer-grey); margin: 0 14px 0 24px; }
  .brand-name { font-size: 42px; font-weight: 900; color: var(--green-dark); letter-spacing: 10px; line-height: 1; white-space: nowrap; }
  .brand-line { font-size: 13px; font-weight: 700; color: var(--footer-grey); letter-spacing: 10.2px; margin-top: 8px; white-space: nowrap; }
</style>
</head>
<body>
<main class="sign">
  <svg class="backdrop" viewBox="0 0 1040 1200" aria-hidden="true">
    <defs>
      <linearGradient id="panelShade" x1="0" y1="0" x2="0" y2="1">
        <stop offset="0" stop-color="var(--panel-top)"/>
        <stop offset="1" stop-color="var(--panel-bottom)"/>
      </linearGradient>
    </defs>
    <path class="panel-green" fill="var(--green)" d="M0,0 L428,0 C440,126 500,251 616,318 L0,511 Z"/>
    <path class="swoosh-dark" fill="var(--green-dark)" d="M424,0 C446,200 600,300 800,396 C960,472 1032,520 1040,560 L1040,640 C1010,550 930,498 776,428 C560,330 444,200 434,0 Z"/>
    <path class="panel-dark" fill="url(#panelShade)" d="M0,590 C4,556 30,540 80,528 L660,339 C850,400 1010,470 1040,590 L1040,1060 L0,1060 Z"/>
  </svg>

  <div class="illustration-slot" role="img" aria-label="Decorative cluster of white question marks"></div>

  <h1 class="headline-confused">CONFUSED?</h1>
  <p class="tagline-answers">WE HAVE THE<br>ANSWERS?</p>
  <h2 class="headline-questions">QUESTIONS?</h2>
  <p class="tagline-right">WE HAVE<br>ANSWERS?</p>

  <h3 class="services-title">OUR SERVICES</h3>

  <svg width="0" height="0" style="position:absolute">
    <symbol id="tick" viewBox="0 0 16 16"><path d="M1,8 L6,14 L15,1" fill="none" stroke="#6aa83a" stroke-width="2.4" stroke-linecap="round" stroke-linejoin="round"/></symbol>
  </svg>

  <ul class="service-list list-left">
    <li><svg><use href="#tick"/></svg>Plovance</li>
    <li><svg><use href="#tick"/></svg>Plovance Supplement</li>
    <li><svg><use href="#tick"/></svg>Plovance Advantage</li>
    <li><svg><use href="#tick"/></svg>Truvely. Part A, Part B, Part D</li>
    <li><svg><use href="#tick"/></svg>Social Security</li>
    <li><svg><use href="#tick"/></svg>Turning 65, Annuities</li>
    <li><svg><use href="#tick"/></svg>Fixed Index Annuities</li>
    <li><svg><use href="#tick"/></svg>Rollovers, 401k, 403b</li>
    <li><svg><use href="#tick"/></svg>Investments, Stock Market</li>
    <li><svg><use href="#tick"/></svg>Mutual Funds, Term Insurance</li>
    <li><svg><use href="#tick"/></svg>Life Insurance, Final Expense</li>
    <li><svg><use href="#tick"/></svg>Long Term Care</li>
  </ul>

  <ul class="service-list list-right">
    <li><svg><use href="#tick"/></svg>Mortgage Protection</li>
    <li><svg><use href="#tick"/></svg>403B / 457 Not for Profit Set Up</li>
    <li><svg><use href="#tick"/></svg>403B / TSA Plans</li>
    <li><svg><use href="#tick"/></svg>Annuities</li>
    <li><svg><use href="#tick"/></svg>Asset Protection</li>
    <li><svg><use href="#tick"/></svg>Charitable Giving</li>
    <li><svg><use href="#tick"/></svg>College Funding</li>
    <li><svg><use href="#tick"/></svg>Estate Planning</li>
    <li><svg><use href="#tick"/></svg>Fixed Indexed Annuities</li>
    <li><svg><use href="#tick"/></svg>Guaranteed Income</li>
    <li><svg><use href="#tick"/></svg>IRA &amp; 401(K) Assets and Planning</li>
    <li><svg><use href="#tick"/></svg>IRA 401(K), 403(B) Rollovers</li>
    <li><svg><use href="#tick"/></svg>Lifetime Income Planning</li>
    <li><svg><use href="#tick"/></svg>Retirement Income Planning</li>
    <li><svg><use href="#tick"/></svg>Safe Money Options</li>
    <li><svg><use href="#tick"/></svg>Social Security</li>
    <li><svg><use href="#tick"/></svg>Tactical Asset Allocation</li>
  </ul>

  <footer class="brand">
    <div class="brand-dot" aria-hidden="true"></div>
    <div class="brand-divider" aria-hidden="true"></div>
    <div class="brand-text">
      <div class="brand-name">HALVORN CAPITAL</div>
      <div class="brand-line">INSURANCE AND FINANCIAL SERVICES</div>
    </div>
  </footer>
</main>
</body>
</html>
```